Glostiva: Graphic elements & webpage layout

Hi there! We’re building a site called Glostiva.example—it will be a community site for beauty product reviews, product recommendations and beauty tutorials. We've already got a logo, thanks to another CraftHive project. This project on CraftHive involves the following web design work:

1) Propose the overall graphic design elements of our site (according to our guidelines, which are in the attached file)

-Color Palette
-Fonts
-Icon set(s)

2) Using the overall graphic design elements in step 1 and our storyboard (attached), develop a webpage layout for the "How-to" page of our site. The "How-to" pages will be an editorial format, where our beauty journalist will show a video (and photos) of step-by-step beauty tutorials.

Please take a look at the attached files for a detailed brief and the logo! Thanks and we're looking forward to working with you!

Target Market(s)

Glostiva is for a French, English, and American audience of women between the ages of 16 and 30, who buy and use beauty products regularly.

Industry/Entity Type

Graphic Design

Requirements
Must have
• 1) A global set of graphic standards for the website Glostiva.example:
• A color palette
• Fonts
• An icon set (or sets)
• A menu
• Other graphic elements like button styles

2) A webpage layout (non-coded) for the How-To page template
(See storyboard, attached separately)
This webpage layout is for the main editorial format on Glostiva—step by step beauty tutorials. The individual on-page elements are in the storyboard, but overall we’d like it to look clean, friendly, and to encourage community participation and sharing on social networks.
Nice to have
• • A look and feel that is fresh, clean and modern
• Proximity: Establishes a close proximity with the user. (We want them to get the same feeling they get when talking beauty tips with their close friends).
• Neutrality: A sincere and neutral look and feel that doesn’t suggest a preference for any particular or elite type of beauty (but it can still be fun!)
• The graphic design is relevant to the beauty sector as a whole. (We could be talking about lipstick, a hairbrush or a man’s cologne)
• The graphic design alludes to the beauty industry (discreetly, not overtly!)
Should not have
• We've already got a logo, so you shouldn't suggest a new one!

We really want to avoid designs that are too traditionally "beauty" or too girly and feminine. Please no pink, no flowers, etc! :)

```html
<!DOCTYPE html>
<html lang="fr">
<head>
<meta charset="utf-8">
<title>Glostiva – Look : Art of nude</title>
<link rel="stylesheet" href="https://fonts.googleapis.com/css2?family=Arvo:wght@400;700&family=Lora:wght@400&family=Arimo:wght@400;700&family=Dancing+Script:wght@600&display=swap">
<style>
:root{
  --teal:#1fc7b0;
  --teal-soft:#c9f1ea;
  --orange:#f6ad62;
  --peach:#fde9d6;
  --peach-side:#fdf1e7;
  --page:#fffbf7;
  --ink:#1d1d1d;
  --grey:#8f8f8f;
  --line:#e9ddd2;
  --bar:#111;
}
*{margin:0;padding:0;box-sizing:border-box}
html,body{width:1136px;height:1200px;overflow:hidden}
body{position:relative;background:var(--peach-side);font-family:"Arimo",Arial,sans-serif;color:var(--ink)}
.abs{position:absolute}
.page-column{left:200px;top:20px;width:736px;height:1180px;background:var(--page)}
.guide{top:20px;width:1px;height:1180px;background:#f0dccb}
.topbar{left:0;top:0;width:1136px;height:20px;background:var(--bar);border-bottom:3px solid var(--teal)}
.social-links{right:270px;top:4px;display:flex;gap:14px;font-size:9px;font-weight:700;color:#777;white-space:nowrap}
.lang{top:1px;width:20px;height:14px;border-radius:2px;font-size:8px;line-height:14px;text-align:center;color:#fff}
.brand{left:220px;top:32px;font-family:"Arvo",serif;font-weight:700;font-size:46px;color:var(--ink);letter-spacing:-1px}
.brand-dot{left:386px;top:36px;width:14px;height:14px;border-radius:50%;background:var(--teal)}
.nav a{position:absolute;top:50px;font-family:"Arvo",serif;font-weight:700;font-size:16px;color:var(--ink);text-decoration:none;padding-left:22px;white-space:nowrap}
.nav a::before{content:"";position:absolute;left:0;top:1px;width:16px;height:16px;border-radius:50%;background:var(--teal)}
.search{left:716px;top:48px;width:200px;height:24px;border-radius:4px;background:#eee9e4;font-family:"Dancing Script",cursive;font-size:16px;color:#c8c2bc;padding:2px 10px}
.search svg{position:absolute;right:8px;top:5px}
.header-rule{left:207px;top:106px;width:713px;height:6px;background:linear-gradient(#efe6dd,transparent)}
.crumb{left:220px;top:115px;font-size:8px;color:var(--grey)}
.title-row{left:220px;top:137px;display:flex;align-items:center;gap:3px;white-space:nowrap}
.title{font-family:"Arvo",serif;font-weight:400;font-size:22px;line-height:28px;margin-right:6px}
.share{display:block;width:14px;height:14px;border-radius:2px}
.like{display:block;width:46px;height:14px;border:1px solid #b7c4d8;border-radius:2px;font-size:8px;line-height:12px;padding-left:16px;color:#3b5998;background:#eef1f7;margin-left:2px}
.count{display:block;width:14px;height:14px;border:1px solid #bbb;font-size:8px;line-height:12px;text-align:center;background:#fff;margin-left:4px}
.meta{left:220px;top:170px;font-size:8px;font-weight:700;letter-spacing:.3px;white-space:nowrap}
.meta span{font-family:"Lora",serif;font-weight:400;color:var(--teal);font-size:9px;margin-right:10px}
.diff{display:inline-block;width:8px;height:8px;border-radius:50%;background:var(--teal);margin-right:2px;vertical-align:-1px}
.hero-panel{left:207px;top:191px;width:433px;height:249px;background:var(--teal-soft)}
.hero-media{left:220px;top:203px;width:407px;height:225px;border:4px solid var(--teal);border-radius:4px;background:linear-gradient(135deg,#f6d3d6,#f3bcae 55%,#f8e2dc)}
.needs-title{left:653px;top:200px;font-family:"Dancing Script",cursive;font-size:18px;color:var(--teal);white-space:nowrap}
.needs{left:658px;top:229px;list-style:none}
.needs li{position:relative;height:36px;padding-left:26px;font-size:8px;font-weight:700;white-space:nowrap}
.needs li small{display:block;font-size:6px;font-weight:400;color:var(--grey);margin-top:2px}
.needs li i{position:absolute;left:4px;top:0;width:8px;height:24px;border-radius:2px}
.intro{left:220px;top:452px;width:409px;font-family:"Lora",serif;font-size:10.5px;line-height:16px;text-align:justify;letter-spacing:-.15px}
.sep{left:207px;width:713px;height:10px;background:linear-gradient(#f0e4d8,transparent)}
.step-label{left:220px;font-family:"Dancing Script",cursive;font-size:30px;color:var(--orange)}
.step-panel{left:207px;width:433px;background:var(--peach)}
.tab{height:12px;font-size:7px;font-weight:700;text-align:center;line-height:12px;color:#b69b85;border-radius:3px 3px 0 0}
.tab.on{background:#f9c99a;color:#fff}
.tab.off{background:#fff}
.media{border:4px solid var(--orange);border-radius:4px}
.video{left:220px;top:609px;width:407px;height:224px;background:linear-gradient(120deg,#e9d0b2,#c68b5b 40%,#e3611e 62%,#4a3324)}
.player{left:228px;top:810px;width:391px;height:14px;border-radius:3px;background:rgba(255,255,255,.9)}
.player .bar{position:absolute;left:26px;top:6px;width:340px;height:2px;background:#e0c4a8}
.player .play{position:absolute;left:4px;top:2px;width:14px;height:10px;background:var(--orange);border-radius:2px}
.photo{left:220px;top:1063px;width:407px;height:140px;background:linear-gradient(90deg,#2b2622 30%,#dcc3ac 45%,#f2d8c4)}
.product{width:110px;text-align:left;font-size:8px;white-space:nowrap}
.product .shot{width:110px;height:92px;margin-bottom:6px}
.product small{display:block;font-size:6px;color:var(--grey)}
.price{font-size:9px;color:var(--orange);font-weight:700}
.buy{display:inline-block;margin-left:4px;padding:0 5px;border-radius:6px;background:var(--orange);color:#fff;font-size:7px;line-height:11px}
.howto h3{font-family:"Lora",serif;font-weight:400;font-size:12px;margin-bottom:4px}
.howto p{font-size:8.5px;line-height:13px;color:var(--grey);margin-bottom:10px}
.howto em{font-style:normal;color:var(--orange)}
.cloud{height:26px;border-radius:14px}
</style>
</head>
<body>
<div class="abs guide" style="left:64px"></div>
<div class="abs guide" style="left:140px"></div>
<div class="abs page-column"></div>
<div class="abs guide" style="left:989px"></div>
<div class="abs guide" style="left:1067px"></div>

<div class="abs cloud" role="img" aria-label="Orange cloud decoration" style="left:102px;top:198px;width:78px;background:#fcc77a"></div>
<div class="abs cloud" role="img" aria-label="Teal cloud decoration" style="left:34px;top:342px;width:56px;background:#1cb8a6"></div>
<div class="abs cloud" role="img" aria-label="Mint cloud decoration" style="left:110px;top:616px;width:64px;background:#7ee0c9"></div>
<div class="abs cloud" role="img" aria-label="Grey cloud decoration" style="left:28px;top:930px;width:72px;background:#dcdcdc"></div>
<div class="abs cloud" role="img" aria-label="Orange cloud decoration" style="left:114px;top:1044px;width:46px;background:#f8a64e"></div>
<div class="abs cloud" role="img" aria-label="Grey cloud decoration" style="left:1024px;top:108px;width:86px;background:#e2e2e2"></div>
<div class="abs cloud" role="img" aria-label="Mint cloud decoration" style="left:964px;top:316px;width:60px;background:#a6eadb"></div>
<div class="abs cloud" role="img" aria-label="Orange cloud decoration" style="left:948px;top:478px;width:80px;background:#f9a54a"></div>
<div class="abs cloud" role="img" aria-label="Teal cloud decoration" style="left:1038px;top:806px;width:60px;background:#1cb8a6"></div>
<div class="abs cloud" role="img" aria-label="Mint cloud decoration" style="left:1030px;top:1154px;width:74px;background:#7ee0c9"></div>

<header>
  <div class="abs topbar">
    <div class="abs social-links"><span>Friendbook</span><span>Chirper</span></div>
    <span class="abs lang" style="left:874px;background:#555">En</span>
    <span class="abs lang" style="left:896px;background:var(--teal)">Fr</span>
  </div>
  <div class="abs brand">Glostiva</div>
  <div class="abs brand-dot"></div>
  <nav class="nav">
    <a href="#" style="left:545px">How to</a>
    <a href="#" style="left:631px">Tips</a>
  </nav>
  <div class="abs search">rechercher
    <svg width="14" height="14" viewBox="0 0 14 14"><circle cx="6" cy="6" r="4.5" fill="none" stroke="#bbb" stroke-width="1.5"/><path d="M9.5 9.5L13 13" stroke="#bbb" stroke-width="1.5"/></svg>
  </div>
</header>
<div class="abs header-rule"></div>

<main>
  <div class="abs crumb">Accueil &gt; How to &gt; Look : Art of nude</div>
  <div class="abs title-row">
    <h1 class="title">Look : Art of nude</h1>
    <span class="share" style="background:#3b5998"></span>
    <span class="share" style="background:#33ccff"></span>
    <span class="like">J'aime</span>
    <span class="count">3</span>
  </div>
  <div class="abs meta">DIFFICULTÉ : <i class="diff"></i><i class="diff"></i><i class="diff" style="background:#cde"></i>&nbsp; DURÉE : <span>20 minutes</span> OCCASION : <span>Tous les jours</span></div>

  <div class="abs hero-panel"></div>
  <div class="abs hero-media" role="img" aria-label="Portrait photo of the finished nude make-up look"></div>

  <div class="abs needs-title">les produits nécessaires :</div>
  <ul class="abs needs">
    <li><i style="background:#9aa"></i>Base Lumière<small>VELOURA PARIS</small></li>
    <li><i style="background:#222;width:4px;left:6px"></i>Correcteur Soft<small>VELOURA PARIS</small></li>
    <li><i style="background:#b08a4a;height:14px;width:20px;left:0;top:4px;border-radius:50%"></i>Poudre Éclat<small>VELOURA PARIS</small></li>
    <li><i style="background:#333;height:2px;width:22px;left:0;top:8px"></i>Crayon Regard<small>VELOURA PARIS</small></li>
    <li><i style="background:#8e1f2a"></i>Rouge Velours<small>VELOURA PARIS</small></li>
    <li><i style="background:#c4505a"></i>Gloss Miroir<small>VELOURA PARIS</small></li>
  </ul>

  <p class="abs intro">Présentation du look. Lorem ipsum dolor sit amet, maiores ornare ac fermentum, imperdiet ut vivamus a, nam lectus at nunc. Quam euismod sem, semper ut potenti pellentesque quisque. In eget sapien sed, sit duis vestibulum ultricies, placerat morbi amet vel, nullam in lorem vel. Quam sem, semper ut potenti pellentesque. In eget sultricies, placerat.</p>

  <div class="abs sep" style="top:533px"></div>

  <section>
    <div class="abs step-label" style="top:540px">étape 1</div>
    <div class="abs step-panel" style="top:583px;height:264px"></div>
    <div class="abs tab on" style="left:220px;top:596px;width:76px">VIDÉO</div>
    <div class="abs tab off" style="left:298px;top:596px;width:76px">PHOTOS</div>
    <div class="abs media video" role="img" aria-label="Video still of a make-up artist applying foundation backstage"></div>
    <div class="abs player"><span class="play"></span><span class="bar"></span></div>

    <div class="abs product" style="left:653px;top:608px"><div class="shot" role="img" aria-label="Foundation bottle product shot" style="background:linear-gradient(#fff,#e5e9ea)"></div>Base Lumière<small>VELOURA PARIS</small><span class="price">30,- €</span><span class="buy">Acheter</span></div>
    <div class="abs product" style="left:784px;top:608px"><div class="shot" role="img" aria-label="Concealer pen product shot" style="background:linear-gradient(#fff,#ece6e0)"></div>Correcteur Soft<small>VELOURA PARIS</small><span class="price">24,- €</span><span class="buy">Acheter</span></div>
    <div class="abs product" style="left:653px;top:745px"><div class="shot" role="img" aria-label="Loose powder pot product shot" style="background:linear-gradient(#fff,#e8dccb)"></div>Poudre Éclat<small>VELOURA PARIS</small><span class="price">15,- €</span><span class="buy">Acheter</span></div>

    <div class="abs howto" style="left:220px;top:855px;width:409px">
      <h3>1. Lisser le teint</h3>
      <p>Lorem ipsum dolor sit amet, maiores <em>ornare ac</em> fermentum, imperdiet ut vivamus a, nam lectus at nunc. Quam euismod sem, semper ut potenti pellentesque quisque. In eget sapien sed, sit duis vestibulum ultricies, morbi amet vel, nullam in lorem vel.</p>
      <h3>2. Illuminer le regard</h3>
      <p>Imperdiet ut vivamus a, <em>nam lectus</em> at nunc. Quam euismod sem, semper ut potenti pellentesque quisque. In eget sapien sed, sit duis vestibulum ultricies, morbi amet vel, <em>nullam in lorem</em> vel.</p>
    </div>
  </section>

  <div class="abs sep" style="top:987px"></div>

  <section>
    <div class="abs step-label" style="top:994px">étape 2</div>
    <div class="abs step-panel" style="top:1037px;height:163px"></div>
    <div class="abs tab off" style="left:220px;top:1050px;width:76px">VIDÉO</div>
    <div class="abs tab on" style="left:298px;top:1050px;width:76px">PHOTOS</div>
    <div class="abs media photo" role="img" aria-label="Backstage photo of the model with the finished look"></div>

    <div class="abs product" style="left:653px;top:1060px"><div class="shot" role="img" aria-label="Lip pencil product shot" style="background:linear-gradient(#fff,#f1e3e3)"></div>Crayon Lèvres<small>VELOURA PARIS</small><span class="price">14,- €</span><span class="buy">Acheter</span></div>
    <div class="abs product" style="left:784px;top:1060px"><div class="shot" role="img" aria-label="Red lipstick product shot" style="background:linear-gradient(#fff,#f0dcdc)"></div>Rouge Velours<small>VELOURA PARIS</small><span class="price">18,- €</span><span class="buy">Acheter</span></div>
  </section>
</main>
</body>
</html>
```